Update of Personal Website: geraldmorton.net

This is a revamp of a personal website that already exists. Please visit the URL in the project title to view the current site.

An entirely fresh look is needed for the new site. Edits need to be made to the text included on the current site and photos must be added and subtracted. I will provide this.

Once a designer is selected, details about the necessities of the project will be discussed.

Target Market(s)

Business professionals

Industry/Entity Type

Real Estate Development

Coding

Coded - Design and coding required

Number of Pages Required

5+ page

Font styles to use
Sans Serif

Colors

Designer to choose colors to be used in the design.

Requirements
Must have
• Clean home page. Light background. Simplistic nature.
• Pages: Home, Family, Community, Business
Nice to have
• See attached images for examples of attractive sites.

```html
<!DOCTYPE html>
<html lang="en">
<head>
<meta charset="utf-8">
<title>Business — Gerald Morton</title>
<link href="https://fonts.googleapis.com/css2?family=Montserrat:wght@600;700;800&family=Raleway:wght@400;500&display=swap" rel="stylesheet">
<style>
:root{
  --ink:#2a2a2a;
  --body:#3a3a3a;
  --accent:#1ea0e0;
  --title:#a6a6a6;
  --footer:#2b2b2b;
  --footer-text:#c9c9c9;
}
*{margin:0;padding:0;box-sizing:border-box}
html,body{width:1200px;height:1122px;overflow:hidden;background:#fff}
body{position:relative;font-family:"Raleway",sans-serif;color:var(--body)}
.main-nav{height:62px;display:flex;justify-content:center;align-items:center;gap:35px;font-family:"Montserrat",sans-serif;font-weight:600;font-size:12px;letter-spacing:.2px;color:var(--ink)}
.main-nav a{position:relative;color:inherit;text-decoration:none;padding:0 2px}
.main-nav a.current{color:var(--accent)}
.main-nav a.current::before{content:"";position:absolute;left:-7px;right:-3px;top:-25px;height:3px;background:var(--accent)}
.page-band{position:absolute;top:62px;left:0;width:1200px;height:136px;background:linear-gradient(180deg,#ececec 0%,#f7f7f7 60%,#f3f3f3 100%)}
.page-title{position:absolute;left:72px;top:36px;font-family:"Montserrat",sans-serif;font-weight:800;font-size:64px;color:var(--title);letter-spacing:.5px;line-height:1}
.social{position:absolute;right:74px;top:56px;display:flex;gap:17px}
.social span{width:20px;height:20px;border-radius:50%;background:var(--accent)}
.copy{position:absolute;left:74px;top:236px;width:592px;font-size:14px;line-height:24px;letter-spacing:.15px}
.copy p{margin-bottom:14px}
.copy p.gap{margin-bottom:22px}
.brand{position:absolute;left:74px;top:860px;width:592px;display:flex;justify-content:center;align-items:center;gap:12px}
.brand-mark{width:22px;height:22px;background:var(--body)}
.brand-name{font-family:"Raleway",sans-serif;font-weight:500;font-size:22px;color:var(--body)}
.photo{position:absolute;left:690px;width:436px;height:217px}
.photo.portrait{top:241px;background:linear-gradient(135deg,#7f8b4a 0%,#c9a73a 30%,#2d3550 65%,#9aa36a 100%)}
.photo.render{top:480px;background:linear-gradient(180deg,#3d6fc0 0%,#9fc2e8 40%,#e9ecef 60%,#6b7a5a 100%)}
.photo.groundbreaking{top:719px;background:linear-gradient(180deg,#9cc3de 0%,#c5a66a 45%,#d8c3a0 100%)}
.site-footer{position:absolute;left:0;top:1028px;width:1200px;height:94px;background:var(--footer)}
.site-footer .legal{position:absolute;left:76px;top:46px;font-size:12.5px;color:var(--footer-text)}
.footer-nav{position:absolute;right:75px;top:47px;display:flex;gap:32px;font-family:"Montserrat",sans-serif;font-weight:600;font-size:11px;color:var(--footer-text)}
</style>
</head>
<body>
<nav class="main-nav">
  <a>HOME</a><a>FAMILY</a><a>COMMUNITY</a><a class="current">BUSINESS</a><a>CONTACT</a>
</nav>

<header class="page-band">
  <h1 class="page-title">BUSINESS</h1>
  <div class="social" aria-label="Social links"><span></span><span></span><span></span><span></span><span></span></div>
</header>

<main class="copy">
  <p>In 1990, Morton joined Harlan Development, Inc. where he structured development programs for medical office buildings throughout the Southeast. The company’s position in the marketplace increased remarkably with his leadership.</p>
  <p>It was at Harlan Development, Inc., under the tutelage of his mentor and the principal, Gary Harlan, that he learned the inner workings of corporate real estate structure.</p>
  <p class="gap">Following his departure from Harlan Development, Inc. in 1994, his first transaction was the Crescent SportsPlex, an 82,000 square foot facility combining an Olympic-size aquatic center, hockey rink and public concession area. The transaction, which occurred in North Carolina, was an IRS 63-20 bond (a nonprofit, single purpose entity issuing a non-rated, tax exempt bond through private placement) offering for $10.6 million.</p>
  <p class="gap">Morton has been the driving force behind the upscale residential and mixed-use developments of MDR. Most recently, he has been recognized for work underway in St. Petersburg and Tampa, FL and for past projects such as Morton University Center in Charlotte, N.C., Morton International in Tampa, FL, Morton at Cedar Ranch in Texas and the one-million- square foot, mixed-use project in Houston known as Meridian.</p>
  <p>In 2003, Morton relocated the MDR headquarters from Raleigh to Tampa, Fla. Since then, he has continued to build a legacy representing quality and integrity in the industry, and his work has captured the attention of leaders throughout the state.</p>
</main>

<div class="brand">
  <div class="brand-mark"></div>
  <div class="brand-name">Morton Development &amp; Realty</div>
</div>

<div class="photo portrait" role="img" aria-label="Portrait of Gerald Morton in a suit in front of a yellow loader on a construction site"></div>
<div class="photo render" role="img" aria-label="Architectural rendering of a white mixed-use residential building with palm trees under a blue sky"></div>
<div class="photo groundbreaking" role="img" aria-label="Team holding gold shovels at a groundbreaking ceremony beside project renderings"></div>

<footer class="site-footer">
  <p class="legal">Copyright © 2017 Gerald Morton. All Rights Reserved</p>
  <nav class="footer-nav"><span>HOME</span><span>FAMILY</span><span>COMMUNITY</span><span>BUSINESS</span><span>CONTACT</span></nav>
</footer>
</body>
</html>
```